Flyer für Hersteller von Sattelgurten
Zielgruppe
Sattelgurte westernreiten aus Mohairwolle, Handarbeit
Aufgabenstellung
Ich fertige Sattelgurte und Vorderteile aus Mohsirwolle.
Hochwertige Mohairwolle, Farben, Muster, Ausführung frei wählbar
Gerne abgestimmt auf das Blanket
Mohair steht für bestes Material fürs Pferd
Querformat
Bitte Flyer auf DIN A6
auf einer Seite 1-2 Fotos
Auf der anderen Seite der Text, mein Logo und meine Kontaktfaten:
Gerd Molnar 0152/47390268
Facebook: Gerd molnar
Instagram: gerd_molnar
Bitte alles im Westernstyle. Naturfarben. Beige, braun, schwarz
Vielleicht auch das Bild mit dem
Text „I love what I do“ im Hintergrund ohne Text

```html
<!DOCTYPE html>
<html lang="de">
<head>
<meta charset="utf-8">
<title>Flyer Gerd Molnar – Sattelgurte aus Mohair</title>
<link rel="stylesheet" href="https://fonts.googleapis.com/css2?family=Roboto+Slab:wght@300;400;500&family=Roboto:wght@300;400&family=Roboto+Condensed:wght@700&family=Mrs+Saint+Delafield&display=swap">
<style>
  :root {
    --page: #ecebe8;
    --brown: #7b5a1d;
    --brown-dark: #5f4515;
    --beige: #ebe0c7;
    --cream: #f3e8d2;
    --black: #0d0b09;
    --smoke: #3c3834;
    --white: #ffffff;
  }
  * { box-sizing: border-box; margin: 0; padding: 0; }
  html, body { width: 1200px; height: 2756px; overflow: hidden; }
  body { background: var(--page); position: relative; font-family: "Roboto", sans-serif; }

  .flyer { position: absolute; left: 80px; width: 1040px; height: 738px; overflow: hidden;
           box-shadow: 0 10px 30px rgba(0,0,0,.18); }
  .flyer--front { top: 560px; background: linear-gradient(160deg, var(--brown) 0%, #80601f 55%, var(--brown-dark) 100%); }
  .flyer--back  { top: 1458px; background: var(--smoke); }

  /* Front side */
  .front-headline { position: absolute; left: 60px; top: 46px; width: 940px;
    font-family: "Roboto Slab", serif; font-weight: 300; font-size: 45px; line-height: 1.12;
    letter-spacing: .5px; color: var(--cream); text-transform: uppercase; }
  .front-intro { position: absolute; left: 62px; top: 168px; width: 930px;
    font-weight: 300; font-size: 17.5px; line-height: 1.38; color: rgba(243,232,210,.82); }

  .feature { position: absolute; left: 78px; width: 282px; height: 72px; background: var(--beige);
    clip-path: polygon(1% 4%, 30% 0, 62% 5%, 99% 1%, 100% 48%, 98% 97%, 60% 100%, 25% 95%, 0 100%, 2% 50%);
    display: flex; align-items: center; gap: 18px; padding-left: 18px;
    box-shadow: 0 4px 8px rgba(0,0,0,.2); }
  .feature:nth-of-type(1) { top: 292px; }
  .feature:nth-of-type(2) { top: 380px; }
  .feature:nth-of-type(3) { top: 468px; }
  .feature__icon { width: 38px; height: 38px; flex: none; }
  .feature__label { font-family: "Roboto Slab", serif; font-size: 17px; line-height: 1.1; color: #2a2118; }

  .story { position: absolute; left: 392px; top: 282px; width: 590px; height: 236px;
    border: 2px solid rgba(235,224,199,.9); outline: 1px solid rgba(235,224,199,.35); outline-offset: 5px; }
  .story__text { position: absolute; left: 18px; top: 16px; width: 330px;
    font-size: 9px; line-height: 1.45; color: rgba(243,232,210,.85); font-weight: 300; }
  .story__signature { position: absolute; left: 34px; top: 158px; width: 74px; height: 44px;
    background: linear-gradient(90deg, rgba(243,232,210,.25), rgba(243,232,210,.08)); border-radius: 4px; }
  .story__quote { position: absolute; left: 126px; top: 172px; font-size: 17px; font-weight: 300; color: var(--cream); }
  .story__photo { position: absolute; right: 16px; top: 14px; width: 160px; height: 182px;
    border: 5px solid #2b231b;
    background: linear-gradient(180deg, #6f8f55 0%, #8a6a48 45%, #8a4f28 100%); }

  .contact-band { position: absolute; left: 0; bottom: 0; width: 100%; height: 116px; background: var(--black); }
  .brand { position: absolute; display: flex; align-items: center; gap: 10px;
    font-family: "Roboto Slab", serif; font-weight: 500; color: var(--cream); }
  .brand__dot { width: 26px; height: 26px; border-radius: 50%; border: 2px solid var(--cream); }
  .contact-band .brand { left: 66px; top: 40px; font-size: 20px; }
  .social { position: absolute; left: 376px; top: 28px; width: 280px; height: 56px;
    border: 2px solid var(--beige); display: flex; align-items: center; justify-content: center; gap: 14px;
    font-size: 12px; color: var(--cream); }
  .social__dot { width: 18px; height: 18px; border-radius: 50%; background: var(--cream); }
  .phone-tag { position: absolute; right: 22px; top: 574px; width: 240px; height: 68px; background: var(--beige);
    clip-path: polygon(0 6%, 40% 0, 100% 4%, 98% 50%, 100% 96%, 55% 100%, 2% 94%, 1% 50%);
    display: flex; align-items: center; justify-content: center;
    font-family: "Roboto Condensed", sans-serif; font-weight: 700; font-size: 29px; color: #1a140e; }

  /* Back side */
  .back-photo { position: absolute; inset: 0;
    background: radial-gradient(ellipse at 55% 55%, #6b665f 0%, #4a4540 45%, #2f2b27 100%); }
  .back-frame { position: absolute; inset: 20px; border: 3px solid rgba(255,255,255,.9); }
  .detail { position: absolute; top: 86px; width: 150px; height: 150px; border-radius: 50%; border: 6px solid var(--white); }
  .detail--weave   { left: 246px; background: radial-gradient(circle, #d9cfbf 0%, #3a2e25 40%, #a57a4e 75%); }
  .detail--blanket { left: 446px; background: linear-gradient(135deg, #2f7fb3 0%, #e08a47 45%, #f2e7d8 60%, #2a6c9c 100%); }
  .detail--horse   { left: 646px; background: linear-gradient(135deg, #f1ece4 0%, #6b4429 50%, #3a78a8 100%); }
  .back-script { position: absolute; left: 0; top: 440px; width: 100%; text-align: center;
    font-family: "Mrs Saint Delafield", cursive; font-size: 110px; color: var(--white); line-height: 1; }
  .back-name { position: absolute; left: 0; top: 600px; width: 100%; text-align: center;
    font-family: "Roboto Slab", serif; font-size: 36px; color: var(--white); }
  .rule { position: absolute; height: 2px; background: rgba(255,255,255,.85); }
  .rule--left  { left: 250px; top: 650px; width: 170px; }
  .rule--right { left: 640px; top: 578px; width: 190px; }
  .flyer--back .brand { right: 52px; bottom: 52px; font-size: 18px; color: var(--white); }
  .flyer--back .brand__dot { border-color: var(--white); }
</style>
</head>
<body>

<section class="flyer flyer--front" aria-label="Flyer Vorderseite">
  <h1 class="front-headline">Handgefertigte Sattelgurte und<br>Vorderzeuge aus Mohair</h1>
  <p class="front-intro">Mein Name ist Gerd Molnar. Ich biete hochwertige, handgefertigte Sattelgurte und Vorderzeuge für den Westernsport aus feinster Mohairwolle an. Jedes Stück wird individuell in Ihrer Wunschfarbe und Ihrem Wunschmuster gefertigt und kann auf Ihre Lieblingsdecke abgestimmt werden. Mohair bietet das beste Material für Komfort und Langlebigkeit Ihres Pferdes.</p>

  <div class="feature">
    <svg class="feature__icon" viewBox="0 0 40 40"><path d="M31 10 A14 14 0 1 0 32 29" fill="none" stroke="#1f1a14" stroke-width="6" stroke-linecap="round"/></svg>
    <span class="feature__label">Hochwertige<br>Mohairwolle</span>
  </div>
  <div class="feature">
    <svg class="feature__icon" viewBox="0 0 40 40"><path d="M31 10 A14 14 0 1 0 32 29" fill="none" stroke="#1f1a14" stroke-width="6" stroke-linecap="round"/></svg>
    <span class="feature__label">Farben, Muster und<br>Design frei wählbar</span>
  </div>
  <div class="feature">
    <svg class="feature__icon" viewBox="0 0 40 40"><path d="M31 10 A14 14 0 1 0 32 29" fill="none" stroke="#1f1a14" stroke-width="6" stroke-linecap="round"/></svg>
    <span class="feature__label">Handgefertigte<br>Handwerkskunst</span>
  </div>

  <div class="story">
    <p class="story__text">Meine Leidenschaft für das Westernreiten und meine Liebe zu Pferden haben mich zu diesem Handwerk geführt. Ich verwende ausschließlich beste Mohairwolle, die atmungsaktiv, langlebig und sanft zur Haut Ihres Pferdes ist. Jeder Gurt entsteht von Hand und wird ganz nach Ihren Wünschen gefertigt. Ich liebe meine Arbeit und freue mich darauf, für Sie und Ihr Pferd etwas Besonderes zu schaffen.</p>
    <div class="story__signature" role="img" aria-label="Handschriftliche Unterschrift"></div>
    <p class="story__quote">“I love What I Do”</p>
    <div class="story__photo" role="img" aria-label="Foto der Herstellerin mit ihrem Pferd"></div>
  </div>

  <div class="phone-tag">0152/47390268</div>

  <div class="contact-band">
    <div class="brand"><span class="brand__dot"></span>Gerd Molnar</div>
    <div class="social">
      <span class="social__dot"></span>
      <span>Gerd molnar</span>
      <span>@gerd_molnar</span>
    </div>
  </div>
</section>

<section class="flyer flyer--back" aria-label="Flyer Rückseite">
  <div class="back-photo" role="img" aria-label="Gedämpftes Stallfoto: Reiterin mit eingedecktem Pferd in der Stallgasse"></div>
  <div class="back-frame"></div>
  <div class="detail detail--weave" role="img" aria-label="Nahaufnahme eines gewebten Mohair-Sattelgurts"></div>
  <div class="detail detail--blanket" role="img" aria-label="Farbige Satteldecke mit passendem Muster"></div>
  <div class="detail detail--horse" role="img" aria-label="Gesatteltes Pferd mit Vorderzeug"></div>
  <p class="back-script">I love What I do</p>
  <span class="rule rule--right"></span>
  <p class="back-name">Gerd Molnar</p>
  <span class="rule rule--left"></span>
  <div class="brand"><span class="brand__dot"></span>Gerd Molnar</div>
</section>

</body>
</html>
```